Business Card Design - Law Firm

We are a boutique law firm located near the beach in Manly, Australia. We have recently had a new logo designed and are revamping our business cards with the new logo.

We have recently had a business card design done for us but are not entirely happy with it. We are looking for something modern, simplistic but striking. We would like to see multiple designs.

We have attached a word document which includes our new logo and the current business card design which we are looking at moving away from.

We would like the business cards to be double sided. We would like the design to include something which we can print in gloss colour when we send it to the business card printers.

```html
<!DOCTYPE html>
<html lang="en">
<head>
<meta charset="utf-8">
<title>Harbourline &amp; Partners Lawyers – Business Card</title>
<link rel="stylesheet" href="https://fonts.googleapis.com/css2?family=Poppins:wght@400;500;600&display=swap">
<style>
  :root {
    --stage: #e9e7e4;
    --brand-blue: #3f4fb8;
    --brand-blue-deep: #3342a6;
    --brand-blue-light: #6f7fd6;
    --gold: #b8a070;
    --paper: #ffffff;
    --ink: #4a4a52;
    --heading: #3f4fb8;
  }
  * { box-sizing: border-box; margin: 0; padding: 0; }
  html, body {
    width: 1200px; height: 716px; overflow: hidden;
    background: var(--stage);
    font-family: "Poppins", sans-serif;
  }
  .stage {
    position: relative; width: 1200px; height: 716px;
    display: flex; align-items: center; justify-content: center; gap: 40px;
  }
  .card {
    position: relative; width: 540px; height: 310px;
    border-radius: 18px; overflow: hidden;
    box-shadow: 0 10px 28px rgba(0,0,0,.18);
  }

  /* Front */
  .card-front {
    background: linear-gradient(150deg, var(--brand-blue-light) 0%, var(--brand-blue) 45%, var(--brand-blue-deep) 100%);
    display: flex; flex-direction: column; align-items: center; justify-content: center;
  }
  .front-brand {
    display: flex; align-items: center; gap: 12px;
    color: #2c3894; font-weight: 600; font-size: 25px; letter-spacing: .3px;
  }
  .brand-dot { width: 14px; height: 14px; border-radius: 50%; background: currentColor; }
  .front-web {
    position: absolute; bottom: 40px; left: 0; right: 0; text-align: center;
    color: #ffffff; font-size: 13px; font-weight: 500; letter-spacing: .3px;
  }

  /* Back */
  .card-back { background: var(--paper); }
  .back-wave { position: absolute; left: 0; bottom: 0; width: 540px; height: 310px; }
  .back-brand {
    position: absolute; left: 34px; top: 118px; width: 200px;
    color: var(--ink); font-weight: 600; font-size: 18px; line-height: 1.3;
  }
  .divider {
    position: absolute; left: 248px; top: 58px; width: 1.5px; height: 140px;
    background: var(--gold);
  }
  .contact { position: absolute; left: 268px; top: 62px; color: var(--ink); }
  .contact-name { color: var(--heading); font-weight: 600; font-size: 19px; line-height: 1.1; }
  .contact-role { font-size: 12px; margin-top: 3px; }
  .contact-address { font-size: 12px; line-height: 1.45; margin-top: 12px; }
  .contact-list { list-style: none; margin-top: 8px; font-size: 12px; line-height: 1.6; }
  .contact-list li { display: flex; align-items: center; gap: 7px; }
  .contact-list svg { width: 11px; height: 11px; fill: var(--brand-blue); flex: none; }
</style>
</head>
<body>
<main class="stage">

  <section class="card card-front" aria-label="Card front">
    <div class="front-brand"><span class="brand-dot"></span>Harbourline &amp; Partners Lawyers</div>
    <p class="front-web">www.harbourlinepartners.com.au</p>
  </section>

  <section class="card card-back" aria-label="Card back">
    <svg class="back-wave" viewBox="0 0 540 310" aria-hidden="true">
      <path d="M0 214 C120 262 300 262 540 292 L540 310 L0 310 Z" fill="var(--brand-blue)"/>
      <path d="M0 196 C130 238 300 244 540 276" fill="none" stroke="var(--gold)" stroke-width="5"/>
      <path d="M0 206 C125 250 300 252 540 284" fill="none" stroke="#d9dbe8" stroke-width="3"/>
    </svg>

    <div class="back-brand">Harbourline &amp; Partners Lawyers</div>
    <div class="divider"></div>

    <div class="contact">
      <h1 class="contact-name">NADIA FORBES</h1>
      <p class="contact-role">Practice Manager</p>
      <p class="contact-address">Suite 4, 12 Marlin Street<br>SEACLIFF NSW 2190</p>
      <ul class="contact-list">
        <li><svg viewBox="0 0 24 24"><path d="M6.6 10.8a15 15 0 0 0 6.6 6.6l2.2-2.2c.3-.3.7-.4 1-.2 1.1.4 2.3.6 3.6.6.6 0 1 .4 1 1V20c0 .6-.4 1-1 1A17 17 0 0 1 3 4c0-.6.4-1 1-1h3.5c.6 0 1 .4 1 1 0 1.3.2 2.5.6 3.6.1.3 0 .7-.2 1z"/></svg>(02) 9000 4817</li>
        <li><svg viewBox="0 0 24 24"><path d="M3 5h18v14H3zm2 2v.5l7 4.5 7-4.5V7zm0 2.9V17h14V9.9l-7 4.5z"/></svg>nadia.forbes@harbourlinelaw.com.au</li>
        <li><svg viewBox="0 0 24 24"><path d="M12 2a10 10 0 1 0 0 20 10 10 0 0 0 0-20zm0 5a5 5 0 1 1 0 10 5 5 0 0 1 0-10z"/></svg>www.harbourlinepartners.com.au</li>
      </ul>
    </div>
  </section>

</main>
</body>
</html>
```